Martial Arts Website

Redevelopment of existing martial arts website.

The academy teaches traditional shaolin martial arts, including Shaolin Kung Fu, Wu Shu, Tai Chi, Qigong and Wing Chun and the site needs to reflect the traditional roots (eg, no tacky boxing imagery)

Existing website is www.copperheron.com.au to get a feel for the desired color scheme (black, green and red). The exact colors can be tweaked though. Please only reuse the logo and font (Karate) - there isnt anything else from the current design that needs to remain.

The current website includes links to a ViewTube channel that includes demonstrations of the training conducted to better guide the design.

The new website site map will be:
1. Home
2. Programs - summary page describing each form of training
a. Tiny Otters
b. Kids Kung Fu
c. Youth Kung Fu
d. Adults Kung Fu
e. Wing Chun
f. Tai Chi & Qigong
g. Weaponry Classes
h. 72 Arts of Shaolin Conditioning Program
i. Acrobatics and Wu Shu
j. Fitness Boxing
3. Timetable
4. Coaches - summary page describing all coaches
a. Sifu (Master)
b. Sihing Lou
c. Sihing Kim
d. Sihing Felix
X. ... up to 10 or so coaches
5. Member Zone
6. Contact Us
Updates

Logo now attached to brief - sorry I only have it in PDF

Just to clarify, I am only expecting a PSD design - no HTML required

Reason: Thanks for the designs, we love a lot of them just require a little extra time to tweak the designs and establish the potential. Thanks for your understanding and efforts.

Target Market(s)

Parents, teenagers, young adults, adults, elderly

Industry/Entity Type

Training

Requirements
Must have
• Chinese kung fu dragon imagery throughout the background
Links to Friendbook and ViewTube channel
Promo/icon in the header "Try 2 free classes now"
Home page should include an embedded ViewTube video

```html
<!DOCTYPE html>
<html lang="en">
<head>
<meta charset="utf-8">
<title>Copper Heron Martial Arts Academy</title>
<link href="https://fonts.googleapis.com/css2?family=PT+Sans:wght@400;700&family=Caesar+Dressing&display=swap" rel="stylesheet">
<style>
:root{
  --bg:#0f130c;
  --panel:#161e12;
  --panel-hi:#25391b;
  --green:#5fbf2a;
  --green-hi:#8ee04a;
  --green-dim:#3d7a1c;
  --olive:#7d8f3a;
  --text:#a3a898;
  --muted:#8c9183;
  --line:#2c3627;
}
*{margin:0;padding:0;box-sizing:border-box}
html,body{width:943px;height:1200px;overflow:hidden;background:var(--bg);font-family:"PT Sans",Verdana,sans-serif;color:var(--text)}
.page{position:relative;width:943px;height:1200px}
.abs{position:absolute}

.brand-mark{left:60px;top:12px;width:90px;height:90px;border-radius:50%;border:4px solid var(--green);background:radial-gradient(circle,#1c2a14,#050805)}
.brand-name{left:158px;top:52px;font-size:37px;font-weight:700;color:var(--green-hi);letter-spacing:.5px;white-space:nowrap}
.tagline{left:330px;top:98px;width:350px;text-align:center;font-size:14px;font-style:italic;color:var(--green-dim)}
.top-icons{left:797px;top:10px;display:flex;gap:17px}
.top-icons span{width:28px;height:28px;display:block}

.promo{left:66px;top:186px;width:100px;height:100px}
.promo p{position:absolute;left:0;top:30px;width:100px;text-align:center;font-size:13px;line-height:14px;color:#f3ffe6;transform:rotate(-18deg)}

.classes{left:204px;top:139px;width:236px;height:354px;background:linear-gradient(90deg,var(--panel) 0%,var(--panel-hi) 100%)}
.classes h2{position:absolute;left:46px;top:36px;font-size:20px;font-weight:400;color:var(--muted);letter-spacing:.5px}
.dash{border-bottom:2px dashed #6b7262;height:0}
.classes .dash{position:absolute;left:28px;top:68px;width:155px}
.classes ul{position:absolute;left:30px;top:80px;list-style:none}
.classes li{font-size:14px;line-height:25px;color:var(--muted);padding-left:21px;position:relative}
.classes li::before{content:"";position:absolute;left:0;top:10px;width:5px;height:5px;background:var(--olive)}

.hero{left:440px;top:170px;width:445px;height:323px;background:radial-gradient(ellipse at 60% 60%,#5a5d58 0%,#2a2c28 35%,var(--bg) 70%)}

.nav{left:217px;top:505px;width:524px;height:51px;border-radius:4px;background:linear-gradient(180deg,#59a82a 0%,#2f6a18 60%,#3a7f1d 100%);display:flex;align-items:center;padding-left:19px;gap:28px}
.nav a{font-family:"Caesar Dressing",serif;font-size:18px;color:#12200b;text-decoration:none;display:flex;align-items:center;gap:8px}
.nav a::before{content:"";width:15px;height:15px;border-radius:50%;background:radial-gradient(circle at 40% 35%,#8ef05a,#2c8a14)}

.sidebar{left:60px;top:570px;width:236px;height:557px;background:var(--panel)}
.side-h{position:absolute;left:17px;font-size:20px;color:var(--muted);font-weight:400;letter-spacing:.5px}
.side-d{position:absolute;left:17px}
.news{position:absolute;left:17px;top:57px;width:212px}
.news li{list-style:none;display:flex;gap:21px;font-size:11px;line-height:13px;color:var(--muted);margin-bottom:10px}
.news li span.ico{flex:none;width:24px;height:24px}
.more{position:absolute;font-size:11px;color:var(--olive);letter-spacing:.3px}
.video{position:absolute;left:12px;top:258px;width:212px;height:127px;background:#000}
.video .thumb{position:absolute;left:51px;top:5px;width:103px;height:110px;background:linear-gradient(180deg,#6f5f5c,#5b3f4b 60%,#7a3038)}
.video .bar{position:absolute;left:0;bottom:0;width:212px;height:12px;background:#e4e4e4}
.video .logo{position:absolute;right:5px;top:99px;font-size:10px;color:#ddd}
.social{position:absolute;top:505px;display:flex;gap:22px;left:46px}
.social span{font-size:13px;color:var(--muted)}

.main-h{position:absolute;font-size:20px;font-weight:400;color:var(--muted);letter-spacing:.5px}
.timetable{left:310px;top:634px;width:573px;border-collapse:collapse;background:var(--panel);font-size:11px;color:var(--muted)}
.timetable th{height:40px;font-size:14px;font-weight:400;color:var(--muted);background:#1a2416;border-right:1px solid var(--bg)}
.timetable td{height:64px;border-right:1px solid var(--bg);border-top:1px solid var(--line);vertical-align:middle;line-height:13px}
.timetable td:first-child{padding-left:22px;font-size:12px}
.timetable td.cls{padding-left:25px}
.timetable td.grp{padding-left:16px}
.timetable td.time{text-align:center}
.welcome{left:310px;top:938px;width:573px;font-size:11px;line-height:12.3px;color:var(--muted)}
.welcome p+p{margin-top:12px}
.footer{left:0;top:1166px;width:943px;text-align:center;font-size:11px;color:var(--olive)}
</style>
</head>
<body>
<div class="page">
  <div class="abs brand-mark" role="img" aria-label="Academy emblem"></div>
  <div class="abs brand-name">Copper Heron Martial Arts Academy</div>
  <div class="abs tagline">Traditional kung fu &amp; tai chi center</div>
  <div class="abs top-icons">
    <svg width="28" height="28" viewBox="0 0 28 28" aria-label="Home"><path d="M3 14 14 4l11 10" fill="none" stroke="#2f6fc9" stroke-width="3"/><rect x="7" y="13" width="14" height="12" fill="#dfe6ee"/><rect x="12" y="17" width="5" height="8" fill="#7a4d2a"/></svg>
    <svg width="28" height="28" viewBox="0 0 28 28" aria-label="Phone"><circle cx="14" cy="14" r="13" fill="#6cc52d"/><path d="M8 11q6-5 12 0v3h-3v-2h-6v2H8z" fill="#fff"/><rect x="9" y="15" width="10" height="6" rx="1" fill="#fff"/></svg>
  </div>

  <div class="abs promo">
    <svg width="100" height="100" viewBox="0 0 100 100" aria-hidden="true"><polygon fill="#6fb51f" points="50,2 60,12 74,8 78,22 92,26 88,40 98,50 88,60 92,74 78,78 74,92 60,88 50,98 40,88 26,92 22,78 8,74 12,60 2,50 12,40 8,26 22,22 26,8 40,12"/></svg>
    <p>Try 2 free<br>classes now</p>
  </div>

  <section class="abs classes">
    <h2>CLASSES</h2>
    <div class="dash"></div>
    <ul>
      <li>Tiny Otters</li><li>Kids Kung Fu</li><li>Youth Kung Fu</li><li>Adults Kung Fu</li><li>Wing Chun</li><li>Tai Chi &amp; Qigong</li><li>Weaponry Classes</li><li>72 Arts of Shaolin</li><li>Performance Team</li>
    </ul>
  </section>
  <div class="abs hero" role="img" aria-label="Kung fu practitioner in white silk uniform in a low stance"></div>

  <nav class="abs nav"><a href="#">Home</a><a href="#">About Us</a><a href="#">Members</a><a href="#">Contacts</a></nav>

  <aside class="abs sidebar">
    <h3 class="side-h" style="top:6px">News &amp; Update</h3>
    <div class="dash side-d" style="top:41px;width:150px"></div>
    <ul class="news">
      <li><span class="ico"><svg width="24" height="24" aria-hidden="true"><line x1="3" y1="3" x2="22" y2="21" stroke="#ccc" stroke-width="2"/></svg></span>Lorem ipsum dolor sit amet, consectetuer adipiscing elit.</li>
      <li><span class="ico"><svg width="24" height="24" aria-hidden="true"><line x1="3" y1="3" x2="22" y2="21" stroke="#ccc" stroke-width="2"/></svg></span>Lorem ipsum dolor sit amet, consectetuer adipiscing elit.</li>
      <li><span class="ico"><svg width="24" height="24" aria-hidden="true"><line x1="3" y1="3" x2="22" y2="21" stroke="#ccc" stroke-width="2"/></svg></span>Lorem ipsum dolor sit amet, consectetuer adipiscing elit.</li>
    </ul>
    <span class="more" style="left:147px;top:167px">MORE NEWS!</span>
    <div style="position:absolute;left:44px;top:193px;width:150px;border-top:1px solid var(--line)"></div>
    <h3 class="side-h" style="top:205px">Latest Video</h3>
    <div class="dash side-d" style="top:240px;width:125px"></div>
    <div class="video">
      <div class="thumb" role="img" aria-label="Children in white uniforms at training"></div>
      <svg style="position:absolute;left:87px;top:49px" width="34" height="22" aria-label="Play"><rect width="34" height="22" rx="4" fill="#ddd"/><polygon points="13,5 23,11 13,17" fill="#444"/></svg>
      <span class="logo">ViewTube</span>
      <div class="bar"></div>
    </div>
    <span class="more" style="left:147px;top:403px">MORE VIDEOS!</span>
    <h3 class="side-h" style="top:443px">Conect With Us</h3>
    <div class="dash side-d" style="top:478px;width:150px"></div>
    <div class="social"><span>Friendbook</span><span>ViewTube</span></div>
  </aside>

  <h2 class="main-h" style="left:311px;top:578px">Time Table Of Classes</h2>
  <div class="abs dash" style="left:311px;top:611px;width:215px"></div>
  <table class="abs timetable">
    <tr><th style="width:107px">Days</th><th style="width:224px">Classes</th><th style="width:107px">Group</th><th>Time</th></tr>
    <tr><td>Monday</td><td class="cls">Lorem ipsum dolor sit amet,<br>consectetuer adipiscing elit.</td><td class="grp">Lorem ipsum<br>dolor sit amet,</td><td class="time">7:00 Am to 9:00 PM</td></tr>
    <tr><td>Wednasdy</td><td class="cls">Lorem ipsum dolor sit amet,<br>consectetuer adipiscing elit.</td><td class="grp">Lorem ipsum<br>dolor sit amet,</td><td class="time">7:00 Am to 9:00 PM</td></tr>
    <tr><td>Friday</td><td class="cls">Lorem ipsum dolor sit amet,<br>consectetuer adipiscing elit.</td><td class="grp">Lorem ipsum<br>dolor sit amet,</td><td class="time">7:00 Am to 9:00 PM</td></tr>
  </table>

  <h2 class="main-h" style="left:311px;top:887px">Welcome To CHMA</h2>
  <div class="abs dash" style="left:311px;top:921px;width:175px"></div>
  <div class="abs welcome">
    <p>Lorem ipsum dolor sit amet, consectetuer adipiscing elit. Aenean commodo ligula eget dolor. Aenean massa. Cum sociis natoque penatibus et magnis dis parturient montes, nascetur ridiculus mus. Donec quam felis, ultricies nec, pellentesque eu, pretium quis, sem. Nulla consequat massa quis enim. Donec pede justo, fringilla vel, aliquet nec,</p>
    <p>vulputate eget, arcu. In enim justo, rhoncus ut, imperdiet a, venenatis vitae, justo. Nullam dictum felis eu pede mollis pretium. Integer tincidunt. Cras dapibus. Vivamus elementum semper nisi. Aenean vulputate eleifend tellus. Aenean leo ligula, porttitor eu, consequat vitae, eleifend ac, enim. Aliquam lorem ante, dapibus in, viverra quis, feugiat a, tellus. Phasellus viverra nulla ut metus varius laoreet. Quisque rutrum. Aenean imperdiet. Etiam ultricies nisi vel augue. Curabitur ullamcorper ultricies nisi. Nam eget dui. Etiam rhoncus. Maecenas tempus, tellus eget condimentum rhoncus, sem quam semper libero, sit amet adipiscing sem neque sed ipsum. Nam quam nunc, blandit vel, luctus pulvinar, hendrerit id, lorem. Maecenas nec odio et ante tincidunt tempus. Donec vitae sapien ut libero venenatis faucibus.</p>
  </div>
  <span class="abs more" style="left:820px;top:1119px">MORE INFO!</span>

  <footer class="abs footer">Copyright © 2012 - Copper Heron Martial Arts Pty Ltd. Glenbrook Vale NSW 2790</footer>
</div>
</body>
</html>
```